Presentation card Launchpad KOVA - Tech Incubator from Perú

We need a Design to promote the incubator of technology Startups.
We are in Perú, we work with a string tech filter and develop enterprenurship competencies in the Startup team.
The card is to facilitators and staff memebers of LaunchpadKOVA.
We want a clear, modern, tech and agile Design.

We work to help New enterprises of technology here in Perú, we expect the candidates have a big competencies to Research and develop technological products.

We work using methodologies from QRB, Felstrom, Bellcourt and London univeesities. Our book base is The arte of the venturer.

We work events all year using diferent formats: Gridvane, Marlow prize, OTRV Plan Challenge you can use these logros in your Design.

Set the name, role, email, cell phone number, address.

Example:
// Contact info section
Osvaldo Quintanar
Rapid Prototyping Center Manager
osvaldo.quintanar@kova.edu.pe
(511) 988 437 216

// Address info section
LaunchpadKOVA
Technology-based business incubator
Av. Los Cedrales 475, Surquillo
Lima - Perú
web: launchpad-kova.org.pe
email: launchpad@kova.edu.pe
phone number: (511) 3692548 ext. 4186

// (optional)Lema section
Making happy using technology

// Social network section
facebook: launchpadkovaoficial

Target Market(s)

Enterprenurship, CTO, Investors, Companies interested on open innovation services

Industry/Entity Type

Information Technology

Contact Information for Business Card

Name, Role, Email, Cell phone number

Colors

Designer to choose colors to be used in the design.

Requirements
Must have
• Logo forms and colors
Nice to have
• I add pictures of the leaders of incubator
Should not have
• No vertical designs

```html
<!DOCTYPE html>
<html lang="en">
<head>
<meta charset="utf-8">
<title>Launchpad KOVA – Business Card</title>
<link rel="stylesheet" href="https://fonts.googleapis.com/css2?family=Lato:wght@400;700;900&display=swap">
<style>
  :root {
    --stage: #666666;
    --card-dark: #302d2f;
    --card-dark-deep: #262325;
    --card-light: #ffffff;
    --brand-pink: #c2305a;
    --brand-pink-faint: #f9e6ec;
    --text-light: #e6e6e6;
    --text-dark: #262424;
    --photo-top: #3a3638;
    --photo-mid: #5a4a44;
    --photo-suit: #2b3350;
  }
  * { box-sizing: border-box; margin: 0; padding: 0; }
  html, body {
    width: 1200px; height: 900px; overflow: hidden;
    background: var(--stage);
    font-family: "Lato", Arial, sans-serif;
  }
  .stage { position: relative; width: 1200px; height: 900px; }

  .card {
    position: absolute; top: 275px;
    width: 477px; height: 295px;
    overflow: hidden;
    box-shadow: 3px 4px 6px rgba(0,0,0,0.45);
  }
  .card--front {
    left: 121px;
    background: linear-gradient(135deg, var(--card-dark) 0%, var(--card-dark-deep) 100%);
    border-radius: 0 55px 0 55px;
  }
  .card--back {
    left: 620px;
    background: var(--card-light);
    border-radius: 55px 0 55px 0;
  }

  .brand {
    position: absolute; z-index: 2;
    display: flex; align-items: flex-start; gap: 8px;
    font-weight: 900; line-height: 1; letter-spacing: 0.3px;
    text-transform: uppercase; white-space: nowrap;
  }
  .brand__mark {
    width: 12px; height: 12px; margin-top: 7px;
    background: var(--brand-pink); flex: none;
  }
  .brand__name { display: block; }
  .card--front .brand { left: 42px; top: 64px; font-size: 28px; color: var(--text-light); }
  .card--back .brand { left: 118px; top: 92px; font-size: 42px; color: var(--text-dark); }
  .card--back .brand__mark { width: 17px; height: 17px; margin-top: 10px; }

  .contact { position: absolute; z-index: 2; left: 41px; top: 185px; }
  .contact__name {
    font-size: 18px; font-weight: 700; color: var(--text-light);
    letter-spacing: 0.2px; text-transform: uppercase;
  }
  .contact__role { font-size: 14.5px; color: var(--brand-pink); margin-top: 1px; }
  .contact__list { list-style: none; margin-top: 14px; }
  .contact__item {
    display: flex; align-items: center; gap: 6px;
    font-size: 14px; color: var(--text-light); line-height: 19px;
  }
  .contact__icon { width: 13px; height: 13px; fill: var(--brand-pink); flex: none; }

  .portrait {
    position: absolute; z-index: 1;
    left: 256px; top: 78px; width: 221px; height: 217px;
    background:
      radial-gradient(ellipse 55px 72px at 110px 75px, var(--photo-mid) 0%, rgba(90,74,68,0) 100%),
      linear-gradient(180deg, var(--photo-top) 0%, var(--photo-top) 55%, var(--photo-suit) 100%);
  }

  .backdrop-block {
    position: absolute; left: 285px; top: 205px; width: 200px; height: 82px;
    background: var(--brand-pink-faint);
  }
</style>
</head>
<body>
<main class="stage">

  <section class="card card--front" aria-label="Business card front">
    <div class="brand">
      <span class="brand__name">Launchpad<br>KOVA</span>
      <span class="brand__mark"></span>
    </div>

    <div class="contact">
      <p class="contact__name">Tomas Reyna</p>
      <p class="contact__role">Managing Director</p>
      <ul class="contact__list">
        <li class="contact__item">
          <svg class="contact__icon" viewBox="0 0 16 16" aria-hidden="true">
            <path d="M2 5c0-2 2-3 6-3s6 1 6 3v1h-3V4.5C10 4 9 4 8 4s-2 0-3 .5V6H2zM4 7h8l2 6H2z"/>
          </svg>
          <span>044-318 275 640</span>
        </li>
        <li class="contact__item">
          <svg class="contact__icon" viewBox="0 0 16 16" aria-hidden="true">
            <path d="M1 3h14v10H1z M2 4l6 5 6-5" stroke="#302d2f" stroke-width="1.2"/>
          </svg>
          <span>info@kovamail.com</span>
        </li>
      </ul>
    </div>

    <div class="portrait" role="img" aria-label="Portrait photo of the managing director in a navy blazer"></div>
  </section>

  <section class="card card--back" aria-label="Business card back">
    <div class="brand">
      <span class="brand__name">Launchpad<br>KOVA</span>
      <span class="brand__mark"></span>
    </div>
    <div class="backdrop-block" aria-hidden="true"></div>
  </section>

</main>
</body>
</html>
```